Law firm website marketed direct to many individual clients

I need someone to design a very basic website for a law firm that will be very eye catching. It's going to be a single-paged, scrolling website with a small number of folds. I have uploaded a simple word document that outlines the basics of what I thought could be the layout, but I am open to suggestion on font, size, shades of color, organization, etc. etc. Essentially the website just needs to be a very efficient and visually appealing way of conveying some simple messages.

Target Market(s)

High volumes of individuals who have gotten into a car accident and then google on their phones a lawyer to hire to represent them.

Industry/Entity Type

Legal

Number of Pages Required

1 page

Font styles to use
Serif
Sans Serif

Colors
34a7d7
85cae6
0592cd

Requirements
Must have
• Must be bright and grab the users attention with color scheme and layout. The different sections should be done in such a way that they can fit entirely onto one smart phone or tablet screen.
Nice to have
• I'd like to try and see what it looks like if in the middle somewhere there is a fold that says "MEET YOUR ATTORNEYS" and includes individual photos of two attorneys, one on the left side and one on the right. And then a small bio section on them. I don't want the photos to include a square or rectangle background, I want the person in the photo to be superimposed on top of whatever pattern or background you have in the fold.
Should not have
• Do not want too much text. Anything more than 2 sentences in any single place is unacceptable.

```html
<!DOCTYPE html>
<html lang="en">
<head>
<meta charset="utf-8">
<title>Meridian Law Group</title>
<link href="https://fonts.googleapis.com/css2?family=Open+Sans:wght@300;400;600;700;800&display=swap" rel="stylesheet">
<style>
:root{
  --blue:#0592cd;
  --blue-mid:#34a7d7;
  --blue-light:#85cae6;
  --navy:#22252f;
  --navy-2:#2b2f3a;
  --ink:#333;
  --grey-bg:#f2f2f2;
  --white:#fff;
}
*{margin:0;padding:0;box-sizing:border-box}
html,body{width:1200px;height:2778px;overflow:hidden}
body{font-family:"Open Sans",Arial,sans-serif;color:var(--ink);background:var(--white);position:relative}
.abs{position:absolute}
.btn{position:absolute;display:flex;align-items:center;justify-content:center;color:var(--white);font-size:23px;text-transform:uppercase;letter-spacing:.5px}
.btn b{font-weight:700;margin-left:8px}
.btn--blue{background:var(--blue)}
.btn--dark{background:var(--navy)}

/* header */
.site-header{left:0;top:0;width:1200px;height:83px;background:var(--navy)}
.brand{position:absolute;left:126px;top:12px;color:var(--blue-mid);font-weight:800;text-transform:uppercase;text-align:center;line-height:1}
.brand__top{font-size:32px;letter-spacing:.5px}
.brand__bottom{font-size:21px;margin-top:3px}
.header-phone{left:785px;top:0;width:311px;height:82px;background:var(--blue);display:flex;align-items:center;justify-content:center;gap:14px;color:var(--white);font-size:36px;font-weight:700}

/* hero */
.hero{left:0;top:83px;width:1200px;height:623px;background:linear-gradient(160deg,#4f7590 0%,#3a5d78 45%,#2c465c 100%)}
.hero__inner{position:absolute;left:0;top:0;width:1200px;height:623px;text-align:center;color:var(--white)}
.hero__kicker{position:absolute;top:144px;width:100%;font-size:33px;font-weight:700}
.hero__title{position:absolute;top:180px;width:100%;font-size:90px;font-weight:300;line-height:80px;text-transform:uppercase}
.hero__title b{font-weight:800}
.hero__rule{position:absolute;left:512px;top:362px;width:156px;height:5px;background:var(--white)}
.hero__call{position:absolute;top:446px;width:100%;font-size:35px}
.hero__call b{font-weight:700}
.hero .btn{left:465px;top:510px;width:252px;height:50px;background:#111;font-size:24px;font-weight:600}

/* features */
.features{left:0;top:706px;width:1200px;height:540px;background:var(--grey-bg)}
.feature{position:absolute;top:105px;width:224px;height:211px;background:var(--white);border-bottom:7px solid var(--blue);box-shadow:0 2px 8px rgba(0,0,0,.08);text-align:center}
.feature__icon{position:absolute;left:62px;top:-55px;width:100px;height:100px;border-radius:50%;background:var(--blue);display:flex;align-items:center;justify-content:center}
.feature__title{position:absolute;top:80px;width:100%;color:var(--blue);font-size:18px;font-weight:700;line-height:21px;text-transform:uppercase}
.feature__text{position:absolute;top:134px;left:14px;right:14px;font-size:14px;line-height:20px;color:#555}

/* attorneys */
.attorneys{left:0;top:1074px;width:1200px;height:874px;background:linear-gradient(135deg,#3f93b8 0%,#2d7fa6 50%,#2b7aa0 100%)}
.attorneys__v{position:absolute;left:0;top:0}
.cta-top{left:470px;top:1083px;width:254px;height:52px}
.section-title{position:absolute;width:100%;text-align:center;color:var(--white);font-size:32px;font-weight:300;text-transform:uppercase}
.section-title b{font-weight:700}
.section-rule{position:absolute;left:543px;width:114px;height:4px;background:var(--white)}
.portrait{position:absolute;border-radius:46% 46% 6px 6px;background:linear-gradient(180deg,#c7b3a3 0%,#2a2f3a 55%,#1c2028 100%)}
.bio{position:absolute;top:1717px;width:473px;height:161px;background:rgba(34,37,47,.92);border:3px solid var(--blue-light);text-align:center;color:var(--white)}
.bio__name{margin-top:24px;font-size:17px;font-weight:700;text-transform:uppercase}
.bio__rule{width:52px;height:3px;background:var(--blue-light);margin:14px auto 0}
.bio__text{margin:22px 28px 0;font-size:13px;line-height:22px;color:#d8dbe2}

/* no fee */
.no-fee{left:0;top:1948px;width:1200px;height:284px;background:var(--white)}
.h-blue{position:absolute;color:var(--blue);font-size:28px;text-transform:uppercase}
.h-blue b{font-weight:700}
.h-blue span{font-weight:400}
.small-copy{position:absolute;font-size:13px;line-height:22px;color:#444}
.small-copy a{color:var(--blue);text-decoration:none;font-weight:600}

/* questions */
.questions{left:0;top:2232px;width:1200px;height:381px;background:var(--grey-bg)}

/* footer */
.site-footer{left:0;top:2613px;width:1200px;height:165px;background:var(--navy);border-top:5px solid var(--blue-mid);text-align:center;color:var(--white)}
.site-footer .brand{position:static;margin-top:28px;display:inline-block}
.site-footer .brand__top{font-size:22px}
.site-footer .brand__bottom{font-size:15px}
.footer__rule{width:40px;height:2px;background:var(--blue-mid);margin:8px auto 0}
.footer__addr{font-size:13px;line-height:23px;margin-top:10px}
.footer__addr b{font-weight:700}
</style>
</head>
<body>

<header class="abs site-header">
  <div class="brand"><div class="brand__top">Meridian</div><div class="brand__bottom">Law Group</div></div>
  <div class="abs header-phone">
    <svg width="18" height="32" viewBox="0 0 18 32"><rect x="1" y="1" width="16" height="30" rx="3" fill="#22252f"/><rect x="3.5" y="5" width="11" height="19" fill="#0592cd"/><circle cx="9" cy="27.5" r="1.6" fill="#0592cd"/></svg>
    (504) 555-0148
  </div>
</header>

<section class="abs hero">
  <div class="abs" role="img" aria-label="Photo: people at the scene of a car accident" style="left:0;top:0;width:1200px;height:623px"></div>
  <div class="hero__inner">
    <div class="hero__kicker">ACCIDENT?&nbsp; INJURED?</div>
    <h1 class="hero__title">Your <b>Case</b><br>Your <b>Money</b></h1>
    <div class="hero__rule"></div>
    <div class="hero__call">Call: <b>504-555-0148</b></div>
    <div class="btn">Learn More</div>
  </div>
</section>

<section class="abs attorneys">
  <svg class="attorneys__v" width="1200" height="160" viewBox="0 0 1200 160"><polygon points="0,0 1200,0 600,158" fill="#f2f2f2"/></svg>
</section>

<section class="abs features">
  <div class="feature" style="left:106px">
    <div class="feature__icon"><svg width="48" height="48" viewBox="0 0 48 48"><path d="M6 22 L22 6 L42 6 L42 26 L26 42 Z" fill="#fff" transform="rotate(90 24 24)"/><circle cx="14" cy="14" r="3" fill="#0592cd" transform="rotate(90 24 24)"/><text x="27" y="32" font-family="Open Sans,sans-serif" font-size="17" font-weight="700" fill="#0592cd" text-anchor="middle">$</text></svg></div>
    <div class="feature__title">Low Fees</div>
    <div class="feature__text">We charge less, so you keep more.</div>
  </div>
  <div class="feature" style="left:361px">
    <div class="feature__icon"><svg width="50" height="56" viewBox="0 0 50 56"><circle cx="25" cy="14" r="11" fill="#fff"/><path d="M4 54 C4 36 12 29 25 29 C38 29 46 36 46 54 Z" fill="#fff"/><path d="M25 30 L22 36 L25 50 L28 36 Z" fill="#0592cd"/></svg></div>
    <div class="feature__title">Free Consultation</div>
    <div class="feature__text">It's always free to<br>talk to us.</div>
  </div>
  <div class="feature" style="left:615px">
    <div class="feature__icon"><svg width="30" height="52" viewBox="0 0 30 52"><rect x="2" y="2" width="26" height="48" rx="4" fill="none" stroke="#fff" stroke-width="3"/><rect x="6" y="9" width="18" height="31" fill="#fff"/><circle cx="15" cy="45" r="2" fill="#fff"/></svg></div>
    <div class="feature__title">Get Started Using<br>Only Your Phone</div>
    <div class="feature__text">No need to come to the office, sign up using your phone.</div>
  </div>
  <div class="feature" style="left:872px">
    <div class="feature__icon"><svg width="52" height="46" viewBox="0 0 52 46"><path d="M16 12 H48 V32 H42 V40 L34 32 H16 Z" fill="#fff" opacity=".85"/><path d="M2 4 H34 V24 H16 L8 32 V24 H2 Z" fill="#fff" stroke="#0592cd" stroke-width="2"/><rect x="8" y="10" width="20" height="2.5" fill="#0592cd"/><rect x="8" y="16" width="14" height="2.5" fill="#0592cd"/></svg></div>
    <div class="feature__title">Speak Directly<br>to a Lawyer</div>
    <div class="feature__text">No staff screening. Talk right to a lawyer on your first call.</div>
  </div>
</section>

<div class="btn btn--blue cta-top">Call<b>504-555-0148</b></div>

<h2 class="section-title" style="top:1300px">Meet Your <b>Attorneys</b></h2>
<div class="section-rule" style="top:1353px"></div>

<div class="portrait" role="img" aria-label="Cut-out photo of the first attorney in a dark suit" style="left:191px;top:1407px;width:294px;height:306px"></div>
<div class="portrait" role="img" aria-label="Cut-out photo of the second attorney in a dark suit" style="left:718px;top:1407px;width:282px;height:306px"></div>

<div class="btn btn--dark" style="left:472px;top:1454px;width:256px;height:52px">Call<b>504-555-0148</b></div>

<div class="bio" style="left:107px">
  <div class="bio__name">Lawyer Name</div>
  <div class="bio__rule"></div>
  <p class="bio__text">Lorem ipsum dolor sit amet, consectetur adipisicing elit, sed do eiusmod tempor incididunt ut labore et dolore magna aliqua.</p>
</div>
<div class="bio" style="left:624px">
  <div class="bio__name">Lawyer Name</div>
  <div class="bio__rule"></div>
  <p class="bio__text">Lorem ipsum dolor sit amet, consectetur adipisicing elit, sed do eiusmod tempor incididunt ut labore et dolore magna aliqua.</p>
</div>

<section class="abs no-fee">
  <div class="abs" role="img" aria-label="Cut-out photo of a smiling client giving a thumbs up" style="left:287px;top:30px;width:245px;height:254px;border-radius:45% 45% 4px 4px;background:linear-gradient(180deg,#b89a84 0%,#9a9b94 50%,#7d7f7b 100%)"></div>
  <h2 class="h-blue" style="left:600px;top:103px"><b>No Fee</b> <span>Unless We Win</span></h2>
  <p class="small-copy" style="left:601px;top:147px;width:380px">We don't get paid unless you get paid. It's as simple as that. We let our results do the talking for us.</p>
</section>

<section class="abs questions">
  <h2 class="h-blue" style="left:172px;top:98px"><b>Questions</b> <span>About Anything?</span></h2>
  <p class="small-copy" style="left:172px;top:146px;width:540px">We're here to help. Feel free to call us at <a>504-555-0148</a> to speak to one of our attorneys. With extensive experience in helping clients get the results that they want, our team is always just a phone call away.</p>
  <div class="btn btn--blue" style="left:172px;top:224px;width:256px;height:52px">Call<b>504-555-0148</b></div>
  <div class="abs" role="img" aria-label="Cut-out photo of a smiling support agent wearing a headset" style="left:700px;top:37px;width:310px;height:344px;border-radius:46% 46% 4px 4px;background:linear-gradient(180deg,#6b4a36 0%,#d9b39a 45%,#f4f4f4 100%)"></div>
</section>

<footer class="abs site-footer">
  <div class="brand"><div class="brand__top">Meridian</div><div class="brand__bottom">Law Group</div></div>
  <div class="footer__rule"></div>
  <div class="footer__addr">Sample Office Suite<br>Riverside, LA 70000<br><b>504-555-0148</b></div>
</footer>

</body>
</html>
```